Luxury Bath Flyer

I would like to have a professional Flyer, which would describe a beautiful atmospheric luxury-Bath situation. I am sending you a( screenshot) Flyer Proposal, which shoes my intention and wish how I would like to have it. Please note that Ästhetik and a professional Flyer is very important to me. If possible send a psd.file or a indesign file, in case of we gonna need to change the text. You are also free to make 2 different proposals and one as you would suggest.?(I send you couple pictures, but the main one which I choose on the pdf file, please keep that, it is called " BE-03" - If there is a question please let me know. Looking forward to receive an amazing artwork.Kind Regards Dilek

```html
<!DOCTYPE html>
<html lang="de">
<head>
<meta charset="utf-8">
<title>Wohnwerk – Ihr Exklusives Bad</title>
<link href="https://fonts.googleapis.com/css2?family=Gentium+Book+Plus:wght@400;700&display=swap" rel="stylesheet">
<style>
  :root {
    --orange: #e44a10;
    --orange-text: #e24f17;
    --blue: #1b58a3;
    --gold: #f6c64a;
    --ink: #1e1e1e;
    --paper: #ffffff;
    --stage: #e8e5e0;
  }
  * { box-sizing: border-box; margin: 0; padding: 0; }
  html, body { width: 1200px; height: 1200px; overflow: hidden; background: var(--stage); }
  body { font-family: "Gentium Book Plus", Georgia, serif; }

  .flyer {
    position: absolute; left: 197px; top: 30px;
    width: 806px; height: 1140px; background: var(--paper);
    box-shadow: 0 6px 22px rgba(0,0,0,.25);
    overflow: hidden;
  }

  .hero {
    position: absolute; left: 0; top: 0; width: 806px; height: 428px;
    background: linear-gradient(180deg, #d8d2c8 0%, #cfc7bb 45%, #6b5846 72%, #4a3b2e 100%);
  }
  .brand-box {
    position: absolute; left: 0; top: 0; width: 313px; height: 176px;
    background: var(--paper);
    display: flex; align-items: center; gap: 14px; padding-left: 44px;
  }
  .brand-mark { width: 16px; height: 16px; background: var(--ink); }
  .brand-name { font-weight: 700; font-size: 30px; color: var(--ink); }

  .headline {
    position: absolute; left: 48px; top: 446px; width: 740px;
    font-weight: 700; font-size: 46px; line-height: 53px; color: var(--orange-text);
    white-space: nowrap;
  }

  .gallery {
    position: absolute; left: 0; top: 621px; width: 806px; height: 195px;
    background: var(--blue); display: flex; gap: 10px; padding: 5px 0;
  }
  .gallery .photo { height: 100%; }
  .photo-basin { width: 251px; background: linear-gradient(160deg, #e9e2d6, #c9a883 60%, #f4f2ee); }
  .photo-bowl { width: 282px; background: linear-gradient(160deg, #a5716a, #8a5a55 55%, #c9c4bd); }
  .photo-showroom { width: 253px; background: linear-gradient(160deg, #7e8fa3, #d9d5cf 55%, #514d4b); }

  .benefits {
    position: absolute; left: 0; top: 816px; width: 394px; height: 238px;
    background: var(--paper); padding: 20px 0 0 48px;
  }
  .services {
    position: absolute; left: 394px; top: 816px; width: 412px; height: 238px;
    background: var(--orange); padding: 20px 0 0 55px;
  }
  .section-title {
    display: inline-block; font-size: 23px; font-weight: 400; padding-bottom: 2px;
    border-bottom: 2px solid currentColor; margin-bottom: 14px;
  }
  .benefits .section-title { color: var(--ink); }
  .services .section-title { color: var(--gold); }
  .ticks { list-style: none; }
  .ticks li { display: flex; gap: 16px; font-size: 21px; line-height: 25px; }
  .benefits .ticks li { color: var(--orange-text); margin-bottom: 17px; }
  .services .ticks li { color: #fde9c9; margin-bottom: 9px; }
  .tick { flex: none; width: 16px; height: 16px; margin-top: 5px; }

  .contact-bar {
    position: absolute; left: 0; top: 1054px; width: 806px; height: 86px;
    background: var(--blue); color: #fff; display: flex; align-items: center;
  }
  .contact-item { display: flex; align-items: center; gap: 14px; height: 60px; }
  .contact-phone { padding-left: 52px; width: 311px; font-size: 34px; font-weight: 700; }
  .contact-address { padding-left: 22px; width: 231px; font-size: 17px; font-weight: 700; line-height: 22px; }
  .contact-web { padding-left: 24px; font-size: 17px; }
  .divider { width: 2px; height: 60px; background: #fff; }
  .contact-icon { width: 26px; height: 26px; flex: none; }
</style>
</head>
<body>
<main class="flyer">
  <div class="hero" role="img" aria-label="Luxuriöses Badezimmer mit freistehender Badewanne, Holzboden und hängendem Waschtisch"></div>

  <header class="brand-box">
    <span class="brand-mark"></span>
    <span class="brand-name">Wohnwerk</span>
  </header>

  <h1 class="headline">Ihr Exklusives Bad Zum Fixpreis!<br>Wir Montieren Für Sie...und Das<br>„alles Aus Einer Hand“!</h1>

  <section class="gallery">
    <div class="photo photo-basin" role="img" aria-label="Waschbecken vor Mosaikfliesen mit Tulpen"></div>
    <div class="photo photo-bowl" role="img" aria-label="Aufsatzwaschbecken mit rundem Spiegel vor roter Wand"></div>
    <div class="photo photo-showroom" role="img" aria-label="Badausstellung mit Möbeln und Heizkörpern"></div>
  </section>

  <section class="benefits">
    <h2 class="section-title">IHRE VORTEILE</h2>
    <ul class="ticks">
      <li><svg class="tick" viewBox="0 0 16 16"><circle cx="8" cy="8" r="6.5" fill="none" stroke="#1e1e1e" stroke-width="1.8"/><path d="M5 8.2l2.2 2.2L13.5 3" fill="none" stroke="#1e1e1e" stroke-width="2"/></svg>Individuelle Badplanung</li>
      <li><svg class="tick" viewBox="0 0 16 16"><circle cx="8" cy="8" r="6.5" fill="none" stroke="#1e1e1e" stroke-width="1.8"/><path d="M5 8.2l2.2 2.2L13.5 3" fill="none" stroke="#1e1e1e" stroke-width="2"/></svg>Eigene Handwerker vor Ort</li>
      <li><svg class="tick" viewBox="0 0 16 16"><circle cx="8" cy="8" r="6.5" fill="none" stroke="#1e1e1e" stroke-width="1.8"/><path d="M5 8.2l2.2 2.2L13.5 3" fill="none" stroke="#1e1e1e" stroke-width="2"/></svg>Traumbad erlebniss</li>
    </ul>
  </section>

  <section class="services">
    <h2 class="section-title">UNSERE SERVICES</h2>
    <ul class="ticks">
      <li><svg class="tick" viewBox="0 0 16 16"><circle cx="8" cy="8" r="6.5" fill="none" stroke="#f6c64a" stroke-width="1.8"/><path d="M5 8.2l2.2 2.2L13.5 3" fill="none" stroke="#f6c64a" stroke-width="2"/></svg>Markenbäder zum Online Preis</li>
      <li><svg class="tick" viewBox="0 0 16 16"><circle cx="8" cy="8" r="6.5" fill="none" stroke="#f6c64a" stroke-width="1.8"/><path d="M5 8.2l2.2 2.2L13.5 3" fill="none" stroke="#f6c64a" stroke-width="2"/></svg>Wir montieren für Sie</li>
      <li><svg class="tick" viewBox="0 0 16 16"><circle cx="8" cy="8" r="6.5" fill="none" stroke="#f6c64a" stroke-width="1.8"/><path d="M5 8.2l2.2 2.2L13.5 3" fill="none" stroke="#f6c64a" stroke-width="2"/></svg>Funktionalität und Ästhetik</li>
      <li><svg class="tick" viewBox="0 0 16 16"><circle cx="8" cy="8" r="6.5" fill="none" stroke="#f6c64a" stroke-width="1.8"/><path d="M5 8.2l2.2 2.2L13.5 3" fill="none" stroke="#f6c64a" stroke-width="2"/></svg>Komplettlösungen mit rasche Umsetzung</li>
    </ul>
  </section>

  <footer class="contact-bar">
    <div class="contact-item contact-phone">
      <svg class="contact-icon" viewBox="0 0 26 26"><circle cx="13" cy="13" r="11.5" fill="none" stroke="#fff" stroke-width="2"/><path d="M9 7.5c-1.3 1-1.6 2.6-.6 4.6 1.2 2.4 3.3 4.6 5.6 5.8 2 1 3.5.6 4.5-.7l-2.2-2.2-1.7 1c-1.5-.8-2.8-2.1-3.6-3.6l1-1.7z" fill="#fff"/></svg>
      <span>0800 314 926</span>
    </div>
    <span class="divider"></span>
    <div class="contact-item contact-address">
      <svg class="contact-icon" viewBox="0 0 26 26"><path d="M13 2a8 8 0 0 0-8 8c0 6 8 14 8 14s8-8 8-14a8 8 0 0 0-8-8z" fill="#fff"/><circle cx="13" cy="10" r="3" fill="#1b58a3"/></svg>
      <span>Lindenweg 14,2351<br>Tannhof</span>
    </div>
    <span class="divider"></span>
    <div class="contact-item contact-web">
      <svg class="contact-icon" viewBox="0 0 26 26" fill="none" stroke="#fff" stroke-width="1.6"><circle cx="13" cy="13" r="10"/><ellipse cx="13" cy="13" rx="4.5" ry="10"/><path d="M3 13h20M5 7.5h16M5 18.5h16"/></svg>
      <span>www.<b>wohnwerk-bad</b>.at</span>
    </div>
  </footer>
</main>
</body>
</html>
```